Help a start up law firm make an impression! - Website

We are a property development and conveyancing law firm looking for some to design our website. The initial brief is for 6 pages with scope for on-going work.

Law firms are traditionally quite conservative and we want to break the mold. We want to come across as fun and modern, while still being professional.

A good example is https://quorvantlaw.com.au/. It's professional yet modern.
Updates

Another good site I like in the same industry: https://www.tamberwickconveyancing.com.au/

Target Market(s)

Tech savy home buyers and sellers - generally 30 to 50 years old

Industry/Entity Type

Law Firm

Coding

Coded - Design and coding required

Number of Pages Required

5+ page

Font styles to use
Other font styles liked:
• No idea

Colors
f04a50

Requirements
Must have
• The elements set out in the design brief document

```html
<!DOCTYPE html>
<html lang="en">
<head>
<meta charset="utf-8">
<title>Harcastle Law – Property Development</title>
<link rel="stylesheet" href="https://fonts.googleapis.com/css2?family=Raleway:wght@400;500;600;700;800&family=Roboto+Slab:wght@800;900&family=Oswald:wght@400;500&family=Lato:wght@400;700&display=swap">
<style>
:root{
  --red:#d0415c;
  --red-dark:#b8334d;
  --pink:#f2c4ce;
  --pink-num:#eab2be;
  --navy:#1d3350;
  --navy-deep:#14263e;
  --ink:#333a44;
  --grey:#eeeeee;
  --footer-bar:#dcdcdc;
  --white:#ffffff;
}
*{box-sizing:border-box;margin:0;padding:0}
html,body{width:1200px;height:2980px;overflow:hidden}
body{font-family:"Lato",sans-serif;color:var(--ink);background:var(--white);position:relative}

/* hero */
.hero{position:relative;height:330px;overflow:hidden}
.hero-photo{position:absolute;inset:0;background:linear-gradient(100deg,#2b4463 0%,#3e5674 45%,#5d6f85 70%,#2a3f5a 100%)}
.hero-shade{position:absolute;inset:0;background:rgba(20,35,58,.45)}
.nav{position:relative;display:flex;align-items:center;height:110px;padding:0 24px}
.brand{font-family:"Raleway",sans-serif;font-weight:800;font-size:34px;color:var(--white);letter-spacing:-.5px}
.menu{display:flex;gap:26px;margin-left:50px;list-style:none}
.menu li{font-family:"Oswald",sans-serif;font-size:15px;color:var(--white)}
.menu li.active{color:var(--red)}
.nav-phone{margin-left:auto;display:flex;align-items:center;gap:10px;font-family:"Oswald",sans-serif;font-size:28px;color:var(--white)}
.hero-title{position:relative;text-align:center;font-family:"Roboto Slab",serif;font-weight:900;font-size:64px;color:var(--white);letter-spacing:3px;margin-top:26px;line-height:1}
.hero-sub{position:relative;text-align:center;font-family:"Raleway",sans-serif;font-weight:600;font-size:18px;color:var(--white);margin-top:40px}

/* section headings */
.heading{font-family:"Raleway",sans-serif;font-weight:700;color:var(--red);text-align:center;font-size:44px;letter-spacing:1px}
.rule{display:block;margin:8px auto 0}

/* difference */
.difference{background:#f7f7f7;height:582px;padding-top:38px}
.intro{width:910px;margin:26px auto 0;text-align:center;font-size:14.5px;line-height:18px;color:#444}
.intro p+p{margin-top:18px}
.features{display:flex;gap:24px;justify-content:center;margin-top:36px}
.feature{width:228px;height:162px;background:var(--white);border:2px solid #cfcfcf;display:flex;flex-direction:column;align-items:center;justify-content:center;text-align:center;padding:0 26px}
.feature svg{margin-bottom:10px}
.feature span{font-family:"Raleway",sans-serif;font-weight:700;font-size:13px;line-height:16px;color:#222;text-transform:uppercase;letter-spacing:.5px}
.services-head{margin-top:38px}

/* services grid */
.services{display:grid;grid-template-columns:repeat(5,240px);grid-template-rows:267px 267px;height:534px}
.service{display:flex;flex-direction:column;align-items:center;padding-top:54px;text-align:center;font-size:14px;line-height:18px;color:#444;padding-left:28px;padding-right:28px}
.service svg{margin-bottom:18px}
.service.light{background:linear-gradient(90deg,#fafafa,#f0f0f0)}
.service.dark{background:linear-gradient(90deg,#e2e2e2,#ededed)}
.gap{height:46px;background:#f7f7f7}

/* projects */
.projects{background:var(--red);height:602px;padding-top:56px;text-align:center;color:var(--white)}
.projects-kicker{font-family:"Raleway",sans-serif;font-weight:400;font-size:27px;letter-spacing:1px}
.projects-title{font-family:"Raleway",sans-serif;font-weight:700;font-size:42px;letter-spacing:1px;margin-top:2px}
.project-cols{display:flex;gap:20px;justify-content:center;margin-top:40px}
.project-list{list-style:none;width:420px;display:flex;flex-direction:column;gap:7px}
.project{display:flex;height:62px;background:var(--pink);border:2px solid #f6d9df;text-align:left;color:#222}
.project-num{width:40px;display:flex;align-items:center;justify-content:center;background:var(--pink-num);font-family:"Raleway",sans-serif;font-weight:700;font-size:13px}
.project-body{padding:6px 10px}
.project-body h3{font-family:"Raleway",sans-serif;font-weight:700;font-size:13px}
.project-body p{font-size:10px;line-height:12px}

/* contact */
.contact{position:relative;height:568px;overflow:hidden}
.contact-photo{position:absolute;inset:0;background:linear-gradient(115deg,#1e3654 0%,#233d5e 40%,#2f4a6c 60%,#182c46 100%)}
.contact-inner{position:relative;padding-top:32px}
.contact-icon{display:block;margin:0 auto}
.contact-title{display:flex;align-items:center;justify-content:center;gap:22px;margin-top:6px;font-family:"Raleway",sans-serif;font-weight:400;font-size:38px;letter-spacing:2px;color:var(--white)}
.contact-title b{color:var(--red);font-weight:700}
.form{width:780px;margin:26px auto 0;display:grid;grid-template-columns:1fr 1fr;column-gap:22px;row-gap:26px}
.field{height:42px;background:var(--white);border-radius:3px;font-size:11px;letter-spacing:1px;color:#999;padding:13px 12px;text-transform:uppercase}
.field.message{grid-column:1/3;height:128px}
.send{grid-column:1/3;height:44px;background:var(--red);border-radius:3px;color:var(--white);font-family:"Raleway",sans-serif;font-weight:700;font-size:12px;letter-spacing:1px;display:flex;align-items:center;justify-content:center;margin-top:8px}
.notch{position:absolute;bottom:-1px;left:50%;transform:translateX(-50%)}

/* footer */
.footer{display:flex;height:256px;padding:36px 0 0 98px;background:var(--white)}
.footer h4{font-family:"Raleway",sans-serif;font-weight:700;font-size:16px;color:var(--red);letter-spacing:1px;margin-bottom:16px}
.links{width:328px}
.links ul{list-style:none}
.links li{font-family:"Raleway",sans-serif;font-size:15px;line-height:25px;color:#333;letter-spacing:.5px}
.contact-info{width:380px}
.info{display:flex;gap:14px;font-family:"Raleway",sans-serif;font-size:15px;line-height:20px;color:#333;letter-spacing:.5px;margin-bottom:18px}
.info svg{flex:none;margin-top:2px}
.footer-brand{font-family:"Raleway",sans-serif;font-weight:800;font-size:36px;color:var(--navy-deep);margin-top:48px;margin-left:-12px}
.bottom-bar{height:62px;background:var(--footer-bar);display:flex;align-items:center;padding:0 98px;font-family:"Raleway",sans-serif;font-size:13px;letter-spacing:1px;color:#333}
.social{margin-left:auto;display:flex;gap:12px}
.social span{width:32px;height:32px;border-radius:50%;background:#8b8b8b}
</style>
</head>
<body>

<header class="hero">
  <div class="hero-photo" role="img" aria-label="Building under construction with cranes against the sky"></div>
  <div class="hero-shade"></div>
  <nav class="nav">
    <div class="brand">Harcastle Law</div>
    <ul class="menu">
      <li>Home</li><li>Conveyancing</li><li class="active">Property Development</li><li>News &amp; Knowledge</li><li>About us</li><li>Contact us</li>
    </ul>
    <div class="nav-phone">
      <svg width="22" height="22" viewBox="0 0 24 24"><path fill="#d0415c" d="M6.6 10.8a15 15 0 0 0 6.6 6.6l2.2-2.2a1 1 0 0 1 1-.25 11.4 11.4 0 0 0 3.6.57 1 1 0 0 1 1 1V20a1 1 0 0 1-1 1A17 17 0 0 1 3 4a1 1 0 0 1 1-1h3.5a1 1 0 0 1 1 1c0 1.25.2 2.45.57 3.57a1 1 0 0 1-.25 1z"/></svg>
      (07) 3190 4472
    </div>
  </nav>
  <h1 class="hero-title">PROPERTY DEVELOPMENT</h1>
  <p class="hero-sub">We understand what it takes to make your next property development a success</p>
</header>

<section class="difference">
  <h2 class="heading">OUR DIFFERENCE</h2>
  <svg class="rule" width="232" height="12" viewBox="0 0 232 12"><line x1="0" y1="6" x2="232" y2="6" stroke="#d0415c" stroke-width="1"/><circle cx="116" cy="6" r="5" fill="#fff" stroke="#d0415c"/></svg>
  <div class="intro">
    <p>Harcastle Law is a specialised property development law firm providing strategic legal advice to developers from site acquisition through to bulk conveyancing of finished stock and everything in between.</p>
    <p>As part of the Harcastle Group, we are able to offer integrated, Legal, Development Management and Project Marketing services. By being in the same office, we are able to offer fiercely competitive prices for these services and allow you to rely on our depth of experience to make your development a success.</p>
  </div>
  <div class="features">
    <div class="feature">
      <svg width="52" height="50" viewBox="0 0 52 50"><path d="M6 24 26 6l20 18" fill="none" stroke="#d0415c" stroke-width="5"/><rect x="12" y="24" width="28" height="22" fill="#d0415c"/><rect x="22" y="32" width="8" height="14" fill="#fff"/></svg>
      <span>Specialist property lawyers</span>
    </div>
    <div class="feature">
      <svg width="52" height="50" viewBox="0 0 52 50"><rect x="4" y="32" width="22" height="6" fill="#d0415c"/><rect x="4" y="40" width="22" height="6" fill="#d0415c"/><rect x="6" y="24" width="22" height="6" fill="#d0415c"/><circle cx="34" cy="24" r="14" fill="#d0415c"/><text x="34" y="30" text-anchor="middle" font-family="Lato,sans-serif" font-weight="700" font-size="16" fill="#fff">$</text></svg>
      <span>Flexible fee arrangements</span>
    </div>
    <div class="feature">
      <svg width="56" height="50" viewBox="0 0 56 50"><circle cx="28" cy="9" r="6" fill="#d0415c"/><circle cx="12" cy="16" r="5" fill="#d0415c"/><circle cx="44" cy="16" r="5" fill="#d0415c"/><path d="M18 36a10 12 0 0 1 20 0z" fill="#d0415c"/><path d="M3 42a9 11 0 0 1 18 0zM35 42a9 11 0 0 1 18 0z" fill="#d0415c"/></svg>
      <span>Integrated development management and project marketing services</span>
    </div>
    <div class="feature">
      <svg width="52" height="50" viewBox="0 0 52 50"><rect x="24" y="2" width="26" height="16" rx="3" fill="none" stroke="#d0415c" stroke-width="2.5"/><circle cx="18" cy="24" r="7" fill="#d0415c"/><path d="M4 48a14 14 0 0 1 28 0z" fill="#d0415c"/></svg>
      <span>Commercial advice</span>
    </div>
  </div>
  <h2 class="heading services-head">OUR SERVICES</h2>
  <svg class="rule" width="232" height="12" viewBox="0 0 232 12"><line x1="0" y1="6" x2="232" y2="6" stroke="#d0415c" stroke-width="1"/><circle cx="116" cy="6" r="5" fill="#fff" stroke="#d0415c"/></svg>
</section>

<section class="services">
  <div class="service dark">
    <svg width="64" height="70" viewBox="0 0 64 70"><rect x="8" y="8" width="40" height="54" rx="3" fill="none" stroke="#d0415c" stroke-width="4"/><rect x="20" y="3" width="16" height="9" fill="#d0415c"/><path d="M16 36l7 7 14-16" fill="none" stroke="#d0415c" stroke-width="4"/><path d="M44 56 60 30" stroke="#d0415c" stroke-width="5"/></svg>
    Development site acquisition and due diligence
  </div>
  <div class="service light">
    <svg width="64" height="70" viewBox="0 0 64 70"><rect x="22" y="26" width="36" height="40" fill="none" stroke="#d0415c" stroke-width="3"/><path d="M30 40h20M30 48h20M30 56h14" stroke="#d0415c" stroke-width="3"/><path d="M6 4l22 34" stroke="#d0415c" stroke-width="7"/></svg>
    Off the plan contracts and disclosure
  </div>
  <div class="service dark">
    <svg width="64" height="70" viewBox="0 0 64 70"><rect x="34" y="4" width="28" height="18" rx="3" fill="none" stroke="#d0415c" stroke-width="3"/><circle cx="26" cy="28" r="10" fill="#d0415c"/><path d="M6 66a20 22 0 0 1 40 0z" fill="#d0415c"/></svg>
    Providing advice on title structuring for mixed use and complex developments
  </div>
  <div class="service light">
    <svg width="64" height="70" viewBox="0 0 64 70"><rect x="12" y="4" width="40" height="60" fill="none" stroke="#d0415c" stroke-width="3.5"/><path d="M20 20h24M20 28h24M20 36h24M20 44h16" stroke="#d0415c" stroke-width="3"/><rect x="36" y="48" width="10" height="8" fill="#d0415c"/></svg>
    Caretaking agreements, letting agreements, community management statements and building management statements.
  </div>
  <div class="service dark">
    <svg width="72" height="70" viewBox="0 0 72 70"><path d="M4 24l14-10 14 6 10-6 14 4 12 14-10 10-12-6-16 14-12-8-12-8z" fill="#d0415c"/></svg>
    Joint venture agreements and development agreements
  </div>
  <div class="service light">
    <svg width="72" height="70" viewBox="0 0 72 70"><path d="M4 34 32 10l28 24" fill="none" stroke="#d0415c" stroke-width="6"/><rect x="12" y="34" width="40" height="30" fill="#d0415c"/><circle cx="48" cy="40" r="8" fill="#eee" stroke="#d0415c" stroke-width="3"/><path d="M34 68a14 16 0 0 1 28 0z" fill="#eee" stroke="#d0415c" stroke-width="3"/></svg>
    Real estate agency appointments
  </div>
  <div class="service dark">
    <svg width="64" height="70" viewBox="0 0 64 70"><rect x="10" y="4" width="44" height="58" fill="none" stroke="#d0415c" stroke-width="3.5"/><path d="M18 16h28M18 24h28M18 32h20" stroke="#d0415c" stroke-width="3"/><circle cx="32" cy="46" r="7" fill="#d0415c"/><path d="M28 52l-3 12 7-4 7 4-3-12" fill="#d0415c"/></svg>
    Certification for construction funding
  </div>
  <div class="service light">
    <svg width="64" height="70" viewBox="0 0 64 70"><rect x="14" y="4" width="30" height="44" rx="3" fill="none" stroke="#d0415c" stroke-width="3.5"/><text x="29" y="32" text-anchor="middle" font-family="Lato,sans-serif" font-weight="700" font-size="18" fill="#d0415c">$</text><path d="M22 40h22a8 8 0 0 1 8 8v18H26z" fill="#d0415c"/></svg>
    Bulk lot conveyancing and settlements
  </div>
  <div class="service dark">
    <svg width="70" height="70" viewBox="0 0 70 70"><path d="M4 58 20 38l12 12 14-22 10 10 10-20" fill="none" stroke="#d0415c" stroke-width="6"/><path d="M52 8h16v16" fill="none" stroke="#d0415c" stroke-width="6"/></svg>
    Development site sales
  </div>
  <div class="service light">
    <svg width="70" height="70" viewBox="0 0 70 70"><circle cx="35" cy="35" r="30" fill="none" stroke="#d0415c" stroke-width="4"/><rect x="20" y="16" width="18" height="12" transform="rotate(-35 29 22)" fill="#d0415c"/><path d="M32 30 46 44" stroke="#d0415c" stroke-width="5"/><rect x="16" y="46" width="26" height="6" fill="#d0415c"/></svg>
    Advice on regulatory compliance
  </div>
</section>
<div class="gap"></div>

<section class="projects">
  <p class="projects-kicker">SOME OF THE PROJECTS</p>
  <h2 class="projects-title">OUR LAWYERS HAVE WORKED ON</h2>
  <svg class="rule" width="232" height="12" viewBox="0 0 232 12"><line x1="0" y1="6" x2="232" y2="6" stroke="#fff" stroke-width="1"/><circle cx="116" cy="6" r="5" fill="#d0415c" stroke="#fff"/></svg>
  <div class="project-cols">
    <ol class="project-list">
      <li class="project"><span class="project-num">1</span><div class="project-body"><h3>What is Lorem Ipsum?</h3><p>Lorem Ipsum is simply dummy text of the printing and typesetting industry. Lorem Ipsum has been the industry's standard dummy text</p></div></li>
      <li class="project"><span class="project-num">2</span><div class="project-body"><h3>What is Lorem Ipsum?</h3><p>Lorem Ipsum is simply dummy text of the printing and typesetting industry. Lorem Ipsum has been the industry's standard dummy text</p></div></li>
      <li class="project"><span class="project-num">3</span><div class="project-body"><h3>What is Lorem Ipsum?</h3><p>Lorem Ipsum is simply dummy text of the printing and typesetting industry. Lorem Ipsum has been the industry's standard dummy text</p></div></li>
      <li class="project"><span class="project-num">4</span><div class="project-body"><h3>What is Lorem Ipsum?</h3><p>Lorem Ipsum is simply dummy text of the printing and typesetting industry. Lorem Ipsum has been the industry's standard dummy text</p></div></li>
      <li class="project"><span class="project-num">5</span><div class="project-body"><h3>What is Lorem Ipsum?</h3><p>Lorem Ipsum is simply dummy text of the printing and typesetting industry. Lorem Ipsum has been the industry's standard dummy text</p></div></li>
    </ol>
    <ol class="project-list">
      <li class="project"><span class="project-num">1</span><div class="project-body"><h3>What is Lorem Ipsum?</h3><p>Lorem Ipsum is simply dummy text of the printing and typesetting industry. Lorem Ipsum has been the industry's standard dummy text</p></div></li>
      <li class="project"><span class="project-num">2</span><div class="project-body"><h3>What is Lorem Ipsum?</h3><p>Lorem Ipsum is simply dummy text of the printing and typesetting industry. Lorem Ipsum has been the industry's standard dummy text</p></div></li>
      <li class="project"><span class="project-num">3</span><div class="project-body"><h3>What is Lorem Ipsum?</h3><p>Lorem Ipsum is simply dummy text of the printing and typesetting industry. Lorem Ipsum has been the industry's standard dummy text</p></div></li>
      <li class="project"><span class="project-num">4</span><div class="project-body"><h3>What is Lorem Ipsum?</h3><p>Lorem Ipsum is simply dummy text of the printing and typesetting industry. Lorem Ipsum has been the industry's standard dummy text</p></div></li>
      <li class="project"><span class="project-num">5</span><div class="project-body"><h3>What is Lorem Ipsum?</h3><p>Lorem Ipsum is simply dummy text of the printing and typesetting industry. Lorem Ipsum has been the industry's standard dummy text</p></div></li>
    </ol>
  </div>
</section>

<section class="contact">
  <div class="contact-photo" role="img" aria-label="Looking up at glass office towers in dark blue tones"></div>
  <div class="contact-inner">
    <svg class="contact-icon" width="56" height="54" viewBox="0 0 56 54"><rect x="10" y="2" width="36" height="26" fill="none" stroke="#fff" stroke-width="2.5"/><path d="M16 10h24M16 16h24M16 22h14" stroke="#fff" stroke-width="2"/><path d="M4 22v30h48V22L28 40z" fill="none" stroke="#fff" stroke-width="2.5"/></svg>
    <h2 class="contact-title">
      <svg width="150" height="10" viewBox="0 0 150 10"><line x1="0" y1="5" x2="146" y2="5" stroke="#fff"/><circle cx="4" cy="5" r="3.5" fill="none" stroke="#fff"/></svg>
      <span>GET IN <b>TOUCH</b></span>
      <svg width="150" height="10" viewBox="0 0 150 10"><line x1="4" y1="5" x2="150" y2="5" stroke="#fff"/><circle cx="146" cy="5" r="3.5" fill="none" stroke="#fff"/></svg>
    </h2>
    <div class="form">
      <div class="field">First name*</div>
      <div class="field">Last name*</div>
      <div class="field">E-mail address*</div>
      <div class="field">Phone number*</div>
      <div class="field message">Message</div>
      <div class="send">SEND NOW</div>
    </div>
  </div>
  <svg class="notch" width="180" height="40" viewBox="0 0 180 40"><path d="M0 40C40 40 50 0 90 0s50 40 90 40z" fill="#fff"/><path d="M84 18l6 6 6-6" fill="none" stroke="#d0415c" stroke-width="2.5"/></svg>
</section>

<footer>
  <div class="footer">
    <div class="links">
      <h4>QUICK LINKS</h4>
      <ul><li>Home</li><li>Conveyancing</li><li>Property Development</li><li>News &amp; Knowledge</li><li>About us</li><li>Contact us</li></ul>
    </div>
    <div class="contact-info">
      <h4>CONTACT US</h4>
      <div class="info"><svg width="20" height="20" viewBox="0 0 20 20"><path d="M10 1a7 7 0 0 0-7 7c0 5 7 11 7 11s7-6 7-11a7 7 0 0 0-7-7z" fill="#d0415c"/><circle cx="10" cy="8" r="2.5" fill="#fff"/></svg><span>Level 1, 820 Bramblewood Road,<br>Kestrel Vale, Wendmoor 4199</span></div>
      <div class="info"><svg width="20" height="20" viewBox="0 0 20 20"><circle cx="10" cy="10" r="10" fill="#d0415c"/><path d="M7 6l2 2-1 1.5a6 6 0 0 0 2.5 2.5L12 11l2 2-1.5 1.5C9 14 6 11 5.5 7.5z" fill="#fff"/></svg><span>(07) 3190 4472</span></div>
      <div class="info"><svg width="20" height="20" viewBox="0 0 20 20"><circle cx="10" cy="10" r="10" fill="#d0415c"/><rect x="5" y="6.5" width="10" height="7" fill="#fff"/><path d="M5 6.5l5 4 5-4" fill="none" stroke="#d0415c" stroke-width="1.2"/></svg><span>mail@harcastlelaw.com.au</span></div>
    </div>
    <div class="footer-brand">Harcastle Law</div>
  </div>
  <div class="bottom-bar">
    <span>© COPYRIGHT - 2017 &nbsp;|&nbsp; ALL RIGHTS RESERVED</span>
    <div class="social" aria-label="Social links"><span></span><span></span><span></span><span></span></div>
  </div>
</footer>

</body>
</html>
```